Tralha Caixa Website

Tralha Caixa is a brazilian Self Storage in a Box where customers can store all the clutter that they have out of their houses. We deliver one or more boxes at their homes, they fill the boxes with their stuff and we store it for them.

"Tralha" means something like "mess" in portuguese. So the name would means something like "Junk Crate" or "Junk Crate".

How it works:
1) The customer asks for 1 or more boxes.
2) Tralha Caixa leaves the boxes at their houses
3) The clients fill the boxes with their stuff
4) Customers call Tralha Caixa for the pick up
5) We get the boxes and store them
6) When the customer wants the box back they can order it online or by phone and wait for the box delivery.
-

We have already produced a flyer to launch the service. You can see this flyer at "Project Files".

We want the website to have a startup "look and fell". Here are some websites of similar services that we like very much.
- www.stowquill.example
- www.pakvale.example

We are planning this launching website to have only 2 pages. The Landing Page and a FAQ page. We are producing an explainer video. The proposed designs must think about a special place to place the video.

We are still writing it´s content but you can use the flyer as a reference.

Thanks.
Updates

Reason: The project was refundable but as we have already received good design options, now we are turning it to Non Refundable and giving more time for new designers to send their proposals. Thanks.

Target Market(s)

Young couples having kids
Students
Families in need of more space at home

Industry/Entity Type

Store

Requirements
Must have
• Special place to place the explainer video (still being produced).

How it works drawing. You can use the one on the flyer or draw a new one (recomended).

Transparent box drawings (showing it´s content). I will serve to show the clients what they can store with the service.

Clutter Room Before/After Pic/drawings (showing how the service can benefit the client).

```html
<!DOCTYPE html>
<html lang="pt">
<head>
<meta charset="utf-8">
<title>Tralha Caixa</title>
<link href="https://fonts.googleapis.com/css2?family=Lato:wght@300;400;700;900&display=swap" rel="stylesheet">
<style>
:root{
  --orange:#f39a1e;
  --orange-soft:#fde3bd;
  --blue:#1b6fc2;
  --blue-deep:#155ea8;
  --blue-light:#3d8fe0;
  --blue-soft:#c7def5;
  --ink:#4a4a4a;
  --muted:#777;
  --page:#f4f4f4;
  --white:#fff;
  --icon:#5b5b5b;
  --footer:#333;
  --footer-bar:#2a2a2a;
}
*{margin:0;padding:0;box-sizing:border-box}
html,body{width:1200px;height:2645px;overflow:hidden}
body{font-family:'Lato',sans-serif;color:var(--ink);background:var(--page);position:relative}
.abs{position:absolute}

/* header */
.site-header{position:absolute;left:0;top:0;width:1200px;height:136px;background:var(--white);border-top:3px solid var(--orange)}
.brand{position:absolute;left:86px;top:40px;display:flex;align-items:center;gap:10px}
.brand-mark{width:34px;height:34px;background:var(--blue);border-radius:4px}
.brand-name{font-size:27px;font-weight:700;color:var(--blue)}
.phone{position:absolute;left:905px;top:26px;display:flex;align-items:center;gap:8px;color:var(--orange);font-weight:700;font-size:25px}
.nav{position:absolute;left:580px;top:98px;display:flex;gap:30px;font-size:14px;color:#555}
.nav .active{color:var(--orange);border-bottom:2px solid var(--orange);padding-bottom:4px}
.quote-btn{position:absolute;left:911px;top:88px;width:201px;height:36px;background:var(--orange);color:var(--white);font-weight:700;font-size:17px;display:flex;align-items:center;justify-content:center;border-radius:2px}

/* hero */
.hero-photo{position:absolute;left:0;top:136px;width:1200px;height:346px;background:linear-gradient(180deg,#6d8fb5 0%,#9bb4cc 40%,#b79a86 70%,#8f7e6b 100%)}
.feature-band{position:absolute;left:0;top:482px;width:1200px;height:242px;background:var(--blue)}
.hero-title{position:absolute;left:90px;top:275px;font-size:33px;line-height:38px}
.hero-title .lead{color:var(--orange);font-weight:700;display:block}
.hero-title .sub{color:var(--white);font-weight:300;display:block}
.hero-product{position:absolute;left:520px;top:252px;width:478px;height:283px;background:linear-gradient(160deg,#5f6265,#2f3133);border-radius:12px}

.feature{position:absolute;top:588px;width:330px;display:flex;gap:10px}
.feature-icon{width:84px;height:84px;border-radius:12px;background:var(--white);display:flex;align-items:center;justify-content:center;flex:none}
.feature h3{color:var(--white);font-size:19px;font-weight:700;margin-top:6px}
.feature p{color:var(--white);font-size:13px;line-height:15px;margin-top:2px}
.feature .more{color:var(--orange);font-size:10px;font-weight:700;margin-top:10px;display:block}

/* how it works */
.how-title{position:absolute;left:90px;top:762px;font-size:38px;font-weight:300;color:var(--blue)}
.step-icon{position:absolute;top:835px}
.step-arrow{position:absolute;top:880px}
.step-text{position:absolute;top:952px;width:220px;text-align:center;color:var(--blue);font-size:12.5px;line-height:15px}

/* video */
.video{position:absolute;left:0;top:1050px;width:1200px;height:365px;background:linear-gradient(180deg,#2c2e30,#3b3d3f 50%,#2a2b2d)}
.video-title{position:absolute;width:1200px;top:1166px;text-align:center;color:#e6e6e6;font-weight:400;font-size:38px}
.play{position:absolute;left:565px;top:1222px}

/* transform + pricing */
.section-title{position:absolute;top:1460px;width:490px;color:var(--orange);font-size:22px;line-height:28px;font-weight:400}
.divider-v{position:absolute;left:595px;top:1460px;width:1px;height:410px;background:#ddd}
.shot{position:absolute;top:1543px;width:226px;height:135px;border-radius:8px;border:2px solid #aaa}
.shot-label{position:absolute;top:1684px;width:226px;text-align:center;color:var(--orange);font-size:12px;font-weight:700}
.checks{position:absolute;left:90px;top:1710px;list-style:none;font-size:14px;line-height:22px;color:#444}
.checks li{display:flex;align-items:center;gap:8px}
.checks li::before{content:"";width:11px;height:11px;border-radius:50%;background:var(--blue);flex:none}
.blurb{position:absolute;left:90px;top:1782px;width:450px;font-size:13px;line-height:18px;color:var(--muted)}
.price-card{position:absolute;top:1542px;width:230px;height:293px;border-radius:5px;color:var(--white);overflow:hidden}
.price-card.orange{left:633px;background:var(--orange)}
.price-card.blue{left:884px;background:var(--blue-light)}
.price-art{height:100px;display:flex;align-items:center;justify-content:center}
.price-art span{width:110px;height:80px;border:3px solid var(--blue-deep);background:rgba(255,255,255,.25)}
.price-head{background:var(--orange-soft);color:#444;text-align:center;padding:6px 0;font-size:12px}
.blue .price-head{background:var(--blue-soft)}
.price-head strong{display:block;font-size:18px;text-decoration:underline}
.price-head strong em{font-style:normal;font-size:22px}
.price-row{text-align:center;font-size:11px;line-height:15px;padding:10px 14px;border-bottom:1px solid rgba(255,255,255,.4)}
.price-row:last-child{border:0}

/* security */
.security{position:absolute;left:0;top:1906px;width:1200px;height:400px;background:#efefef}
.badge{position:absolute;left:560px;top:1880px;width:80px;height:80px;border-radius:50%;background:var(--blue);border:6px solid var(--white);box-shadow:0 0 0 2px var(--blue)}
.badge-name{position:absolute;left:0;width:1200px;top:1972px;text-align:center;color:var(--blue);font-weight:700;font-size:16px}
.sec-title{position:absolute;width:1200px;top:2025px;text-align:center;color:var(--blue);font-size:38px;font-weight:400}
.sec-sub{position:absolute;width:1200px;top:2073px;text-align:center;color:var(--blue);font-size:18px}
.sec-text{position:absolute;left:240px;width:720px;top:2101px;text-align:center;color:var(--muted);font-size:13px;line-height:17px}
.hazard{position:absolute;top:2182px;width:76px;height:76px;border-radius:50%;border:3px solid #666;background:var(--white);display:flex;align-items:center;justify-content:center}

/* press */
.press{position:absolute;left:0;top:2306px;width:1200px;height:91px;background:var(--orange)}
.press-badge{position:absolute;top:2340px;height:22px;background:#2b2b2b;border-radius:3px}

/* footer */
.footer{position:absolute;left:0;top:2397px;width:1200px;height:208px;background:var(--footer)}
.foot-title{position:absolute;top:2430px;color:var(--white);font-size:20px;font-weight:400}
.foot-links{position:absolute;left:90px;top:2462px;list-style:none;font-size:12.5px;line-height:19.5px;color:#ccc}
.foot-line{position:absolute;top:2425px;width:1px;height:160px;background:#555}
.contact{position:absolute;left:362px;top:2462px;list-style:none;font-size:12.5px;line-height:18px;color:#ccc}
.contact li{display:flex;gap:10px;margin-bottom:4px}
.contact svg{flex:none;margin-top:3px}
.social{position:absolute;top:2487px;width:38px;height:38px;border-radius:50%;border:2px solid #ccc}
.foot-brand{position:absolute;left:940px;top:2490px;display:flex;align-items:center;gap:10px;color:var(--white);font-size:25px;font-weight:700}
.foot-brand span{width:30px;height:30px;background:#ddd;border-radius:4px}
.foot-bar{position:absolute;left:0;top:2605px;width:1200px;height:40px;background:var(--footer-bar);color:#aaa;font-size:12px}
.foot-bar .left{position:absolute;left:90px;top:13px}
.foot-bar .right{position:absolute;right:88px;top:13px}
</style>
</head>
<body>

<header class="site-header">
  <div class="brand"><span class="brand-mark"></span><span class="brand-name">Tralha Caixa</span></div>
  <div class="phone">
    <svg width="28" height="28" viewBox="0 0 28 28"><circle cx="14" cy="14" r="12" fill="none" stroke="#f39a1e" stroke-width="2"/><path d="M10 8l3 3-2 2c1 2 2 3 4 4l2-2 3 3-2 2c-5 0-10-5-10-10z" fill="#f39a1e"/></svg>
    <span>(21) 3555-0142</span>
  </div>
  <nav class="nav"><span class="active">How it Works</span><span>Pricing</span><span>Security</span><span>Login</span></nav>
  <div class="quote-btn">GET FREE QUOTE</div>
</header>

<div class="hero-photo" role="img" aria-label="Blurred row of colourful beach storage huts under a blue sky"></div>
<div class="feature-band"></div>
<h1 class="hero-title"><span class="lead">Select the box that best fits</span><span class="sub">IN THEIR NEEDS</span></h1>
<div class="hero-product" role="img" aria-label="Large and small dark grey storage boxes"></div>

<div class="feature" style="left:88px">
  <div class="feature-icon"><svg width="62" height="62" viewBox="0 0 62 62"><circle cx="31" cy="31" r="28" fill="#f39a1e"/><circle cx="31" cy="31" r="20" fill="none" stroke="#fff" stroke-width="3"/><path d="M31 18v13l9 6" fill="none" stroke="#fff" stroke-width="3" stroke-linecap="round"/></svg></div>
  <div><h3>Segurança:</h3><p>tenha suas coisas armazenadas em um ambiente seguro, monitorado 24 horas por dia</p><span class="more">READMORE</span></div>
</div>
<div class="feature" style="left:455px">
  <div class="feature-icon"><svg width="62" height="62" viewBox="0 0 62 62"><circle cx="31" cy="31" r="26" fill="none" stroke="#f39a1e" stroke-width="4"/><path d="M19 31l9 9 17-20" fill="none" stroke="#1b6fc2" stroke-width="5" stroke-linecap="round"/></svg></div>
  <div><h3>Praticidade:</h3><p>escolha o recebimento de suas coisas em sua casa ou em um de nossos Pontos de Coleta no Flamengo...</p><span class="more">READMORE</span></div>
</div>
<div class="feature" style="left:798px">
  <div class="feature-icon"><svg width="62" height="62" viewBox="0 0 62 62"><circle cx="31" cy="31" r="28" fill="#f39a1e"/><rect x="17" y="22" width="28" height="20" rx="2" fill="none" stroke="#fff" stroke-width="3"/><circle cx="31" cy="32" r="5" fill="none" stroke="#fff" stroke-width="3"/></svg></div>
  <div><h3>Economia:</h3><p>aproveite melhor o espaço que você já tem dentro de casa</p><span class="more">READMORE</span></div>
</div>

<h2 class="how-title">How it works</h2>
<svg class="step-icon" style="left:113px" width="110" height="110" viewBox="0 0 110 110" role="img" aria-label="Order a box to your home"><circle cx="55" cy="55" r="50" fill="none" stroke="#5b5b5b" stroke-width="4"/><path d="M35 58l20-18 20 18v22H35z" fill="#5b5b5b"/><rect x="50" y="66" width="10" height="14" fill="#f4f4f4"/></svg>
<svg class="step-icon" style="left:377px" width="110" height="110" viewBox="0 0 110 110" role="img" aria-label="Fill and lock the box"><circle cx="55" cy="55" r="50" fill="none" stroke="#5b5b5b" stroke-width="4"/><rect x="30" y="46" width="50" height="34" fill="#5b5b5b"/><path d="M30 46l10-12h30l10 12" fill="none" stroke="#5b5b5b" stroke-width="4"/><rect x="50" y="56" width="10" height="10" fill="#f39a1e"/></svg>
<svg class="step-icon" style="left:665px" width="110" height="110" viewBox="0 0 110 110" role="img" aria-label="Schedule the box pickup"><circle cx="55" cy="55" r="50" fill="none" stroke="#5b5b5b" stroke-width="4"/><rect x="24" y="42" width="40" height="30" fill="#5b5b5b"/><path d="M64 52h12l9 10v10H64z" fill="#5b5b5b"/><circle cx="36" cy="76" r="6" fill="#5b5b5b" stroke="#f4f4f4" stroke-width="2"/><circle cx="74" cy="76" r="6" fill="#5b5b5b" stroke="#f4f4f4" stroke-width="2"/></svg>
<svg class="step-icon" style="left:942px" width="110" height="110" viewBox="0 0 110 110" role="img" aria-label="Request your box back by phone"><circle cx="55" cy="55" r="50" fill="none" stroke="#5b5b5b" stroke-width="4"/><rect x="42" y="28" width="26" height="50" rx="4" fill="#5b5b5b"/><rect x="46" y="34" width="18" height="32" fill="#f4f4f4"/><circle cx="55" cy="72" r="2.5" fill="#f4f4f4"/></svg>
<svg class="step-arrow" style="left:280px" width="44" height="30" viewBox="0 0 44 30"><path d="M0 10h26V0l18 15-18 15V20H0z" fill="#f39a1e"/></svg>
<svg class="step-arrow" style="left:550px" width="44" height="30" viewBox="0 0 44 30"><path d="M0 10h26V0l18 15-18 15V20H0z" fill="#f39a1e"/></svg>
<svg class="step-arrow" style="left:835px" width="44" height="30" viewBox="0 0 44 30"><path d="M0 10h26V0l18 15-18 15V20H0z" fill="#f39a1e"/></svg>
<p class="step-text" style="left:58px">Solicite a Tralha Caixa<br>em sua casa</p>
<p class="step-text" style="left:322px">Guarde tudo o que quiser,<br>tranque a caixa e guarde a<br>chave</p>
<p class="step-text" style="left:610px">Agende a<br>coleta da caixa</p>
<p class="step-text" style="left:887px">Tenha acesso às suas coisas sempre<br>quiser solicitando a entrega da Tralha<br>Caixa em sua casa ou em um de nossos<br>Pontos de Coleta</p>

<section class="video" role="img" aria-label="Dark shipping container doors behind the explainer video"></section>
<h2 class="video-title">Watch How We Work</h2>
<svg class="play" width="70" height="70" viewBox="0 0 70 70"><circle cx="35" cy="35" r="31" fill="none" stroke="#d8d8d8" stroke-width="5"/><path d="M27 21l22 14-22 14z" fill="#d8d8d8"/></svg>

<h2 class="section-title" style="left:90px">Transforme o seu quarto da tralha em um quarto de verdade</h2>
<h2 class="section-title" style="left:620px">Escolha a caixa que melhor se enquadra em suas necessidades:</h2>
<div class="divider-v"></div>
<div class="shot" style="left:90px;background:linear-gradient(135deg,#5d5a58,#2e2b2a)" role="img" aria-label="Cluttered room before storage"></div>
<div class="shot" style="left:342px;background:linear-gradient(135deg,#6b5844,#2f261f)" role="img" aria-label="Tidy room after storage"></div>
<p class="shot-label" style="left:90px">ANTES</p>
<p class="shot-label" style="left:342px">DEPOIS</p>
<ul class="checks">
  <li>A família está crescendo?</li>
  <li>Quer receber bem aquele parente?</li>
  <li>Está se mudando para um lugar menor?</li>
</ul>
<p class="blurb">Reconquiste o espaço da sua casa guardando tudo aquilo que você não usa no seu dia-a-dia com a Tralha Caixa.<br>Não use o precioso espaço da sua casa como depósito. Deixe que a Tralha Caixa guarda as coisas para você.</p>

<div class="price-card orange">
  <div class="price-art" role="img" aria-label="Transparent large box showing stored items"><span></span></div>
  <div class="price-head">a partir de<strong>R$<em>69,00</em> / mês</strong></div>
  <p class="price-row">Dimensões: 120cm (C) x 80cm (L) x 92,5cm (A). Volume total: 800 Litros</p>
  <p class="price-row">Entrega nos pontos de coleta: R$ 9,90</p>
  <p class="price-row">Entrega em domicílio: R$29,90</p>
</div>
<div class="price-card blue">
  <div class="price-art" role="img" aria-label="Transparent small box showing stored items"><span></span></div>
  <div class="price-head">a partir de<strong>R$<em>14,90</em> / mês</strong></div>
  <p class="price-row">Dimensões: 78cm (C) x 56cm (L) x 41cm (A). Volume total: 130 Litros</p>
  <p class="price-row">Entrega nos pontos de coleta: R$ 4,90</p>
  <p class="price-row">Entrega em domicílio: R$14,90</p>
</div>

<section class="security"></section>
<div class="badge"></div>
<p class="badge-name">Tralha Caixa</p>
<h2 class="sec-title">Security is our Priority</h2>
<p class="sec-sub">Professional storage and 24hr security keep your things safe from the hazards at home</p>
<p class="sec-text">We understand how it feels to have things you care about placed in the protection of others, so we've made the security of your boxes the greatest priority at Tralha Caixa. With storage from Tralha Caixa, you're protected from:</p>
<div class="hazard" style="left:347px" role="img" aria-label="Theft"><svg width="44" height="44" viewBox="0 0 44 44"><rect x="4" y="4" width="36" height="36" rx="4" fill="#1b6fc2"/><rect x="9" y="9" width="26" height="26" rx="2" fill="#fff"/><circle cx="22" cy="22" r="7" fill="none" stroke="#f39a1e" stroke-width="3"/></svg></div>
<div class="hazard" style="left:484px" role="img" aria-label="Fire"><svg width="44" height="44" viewBox="0 0 44 44"><path d="M22 4c2 8 12 12 12 24a12 12 0 0 1-24 0c0-7 5-9 6-15 3 3 3 6 3 8 3-4 4-10 3-17z" fill="#f39a1e"/><path d="M22 26c3 3 5 5 5 8a5 5 0 0 1-10 0c0-3 3-5 5-8z" fill="#fff"/></svg></div>
<div class="hazard" style="left:622px" role="img" aria-label="Water damage"><svg width="44" height="44" viewBox="0 0 44 44"><path d="M22 4c6 10 13 17 13 25a13 13 0 0 1-26 0c0-8 7-15 13-25z" fill="#1b6fc2"/><path d="M22 20c3 5 6 8 6 11a6 6 0 0 1-12 0c0-3 3-6 6-11z" fill="#f39a1e"/></svg></div>
<div class="hazard" style="left:762px" role="img" aria-label="Pests"><svg width="44" height="44" viewBox="0 0 44 44"><circle cx="22" cy="22" r="18" fill="none" stroke="#f39a1e" stroke-width="3"/><circle cx="22" cy="22" r="8" fill="#1b6fc2"/><path d="M22 2v10M22 32v10M2 22h10M32 22h10" stroke="#f39a1e" stroke-width="3"/></svg></div>

<section class="press" aria-label="Press mentions"></section>
<div class="press-badge" style="left:300px;width:135px"></div>
<div class="press-badge" style="left:485px;width:95px"></div>
<div class="press-badge" style="left:645px;width:70px"></div>
<div class="press-badge" style="left:777px;width:128px"></div>

<footer class="footer"></footer>
<h4 class="foot-title" style="left:90px">Special Links</h4>
<h4 class="foot-title" style="left:362px">Contact Us</h4>
<h4 class="foot-title" style="left:673px">Follow Us On</h4>
<ul class="foot-links">
  <li>Frequently Asked Questions</li><li>In the Press</li><li>Jobs at Tralha Caixa</li><li>Privacy Policy</li><li>Shipment &amp; Storage</li><li>Terms of Service</li><li>Blog</li>
</ul>
<div class="foot-line" style="left:298px"></div>
<div class="foot-line" style="left:633px"></div>
<div class="foot-line" style="left:882px"></div>
<ul class="contact">
  <li><svg width="12" height="12" viewBox="0 0 12 12"><path d="M2 1l3 3-1.5 1.5c1 2 2 3 3 3L8 7l3 3-1.5 1.5C5 11.5 .5 7 .5 2.5z" fill="#ccc"/></svg>(21) 3555-0142</li>
  <li><svg width="12" height="10" viewBox="0 0 12 10"><rect x="0.5" y="0.5" width="11" height="9" fill="none" stroke="#ccc"/><path d="M1 1l5 4 5-4" fill="none" stroke="#ccc"/></svg>info@TralhaCaixa.example</li>
  <li><svg width="12" height="14" viewBox="0 0 12 14"><path d="M6 0a5 5 0 0 1 5 5c0 4-5 9-5 9S1 9 1 5a5 5 0 0 1 5-5z" fill="#ccc"/><circle cx="6" cy="5" r="2" fill="#333"/></svg><span>Tralha Caixa Simple Urban Storage<br>88 Marlow Ave, 3rd Fl<br>Rivertown, RT 20415</span></li>
</ul>
<div class="social" style="left:670px"></div>
<div class="social" style="left:724px"></div>
<div class="social" style="left:778px"></div>
<div class="foot-brand"><span></span>Tralha Caixa</div>
<div class="foot-bar"><span class="left">© 2013, Tralha Caixa.Com</span><span class="right">Terms | Privacy</span></div>

</body>
</html>
```